www.trelvonventuresgq.com

Design a professional Project Investor Pitch that give me the bestest and incredible WOW factor and its really Piques the INVESTER interest within first 2/3 slides of this businesse investor pitch

Target Market(s)

To reach INVESTORS that are Island minded and has knowledge of Philippines and want to see local economy grow and reduce foreign control of philippine islands and much more

Industry/Entity Type

Construction of Recycling Plant on Top 5 islands of the philippines

Font styles to use
Other font styles liked:
• Surprise me Designer :)

Colors

Designer to choose colors to be used in the design.

Requirements
Must have
• Plz check out my website and the attachments l sent .....its has to be be just like that pitch l sent to you but will need a updated version and the great WOW factor (just like in attachment 8) that wil grab Investors interest and keeness to be part of my projects company l have my origional pitch version and by all my create another one if u can do it better with the charts and bar graphs ...it must have exact same details on these charts/bar graphs in wording and details..it ya can create an amazing WOW factor investor pitch ...hit me with it !! Plz use the stats in the (Odari Investor Pitch) attachment 2 and input some bottling numbers as written but in charts/bar graphs format...
Nice to have
• just back yourself and give me the biggest WOW factor (like attachment 8) u can with exact same wording on the charts/bar graphs...just gimme best INVESTOR PiTCH ....think of this busines pitch as if your blood in your body absolutely depended on it !!!
Should not have
• Nothing misleading or illegal intent ....as this pitch is based on "Untapped Market" ..as its has Waste management but NO-ONE recyles the plastics / glasses/ cardboards etc ...Plz dont put in charts or bar graphs that are not true or illegal or misleading

```html
<!DOCTYPE html>
<html lang="en">
<head>
<meta charset="utf-8">
<title>Trelvon Ventures – Boracay Recycling Plant 2026 Investor Pitch</title>
<link rel="stylesheet" href="https://fonts.googleapis.com/css2?family=Poppins:wght@400;500;600;700&display=swap">
<style>
:root{
  --green:#3aaa3f;
  --green-dark:#2f8f33;
  --orange:#f9ae3b;
  --red:#e5262b;
  --blue:#2a9fe0;
  --ink:#222222;
  --muted:#555555;
  --panel:#f1f1f1;
  --canvas:#efefef;
}
*{box-sizing:border-box;margin:0;padding:0}
html,body{width:821px;height:1200px;overflow:hidden;background:var(--canvas)}
body{position:relative;font-family:'Poppins',sans-serif;color:var(--ink)}
.slide{position:absolute;width:344px;height:193px;overflow:hidden;background:#fff;box-shadow:0 2px 6px rgba(0,0,0,.12)}
.col-a{left:50px}.col-b{left:426px}
.row-1{top:38px}.row-2{top:269px}.row-3{top:499px}.row-4{top:730px}.row-5{top:960px}
.abs{position:absolute}
.brand{position:absolute;left:12px;top:9px;display:flex;align-items:center;gap:2px;font-size:3.2px;font-weight:600;letter-spacing:.4px;color:var(--orange)}
.brand i{display:block;width:5px;height:5px;border-radius:50%;background:var(--green)}
.tag{position:absolute;right:12px;top:11px;width:11px;height:4px;background:var(--orange)}
.pageno{position:absolute;right:12px;bottom:6px;font-size:3.5px;color:#999;display:flex;align-items:center;gap:3px}
.pageno i{width:4px;height:4px;border-radius:50%;background:var(--orange);box-shadow:0 0 0 1px #fde1b3}
.title{font-weight:600;font-size:13.5px;line-height:1.1;color:var(--ink)}
.title em{font-style:normal;color:var(--orange)}
.rule{position:absolute;width:15px;height:1.3px;background:var(--ink)}
.photo{position:absolute}
.btn{position:absolute;background:var(--green);color:#fff;font-weight:600;border-radius:3px;display:flex;align-items:center;justify-content:center}
.small{font-size:4.2px;line-height:1.55;color:var(--muted)}
.tick{display:inline-block;width:6px;height:6px;border-radius:50%;background:var(--orange);position:relative;flex:none}
.tick::after{content:"";position:absolute;left:1.9px;top:1.2px;width:1.5px;height:2.6px;border:solid #fff;border-width:0 .7px .7px 0;transform:rotate(45deg)}
.check-row{position:absolute;display:flex;gap:4px;align-items:flex-start;font-size:4.2px;color:#444;line-height:1.6}
/* budget */
.bar-row{position:absolute;left:0;height:5.4px;display:flex;align-items:center}
.bar-label{position:absolute;left:33px;font-size:4px;font-weight:600;color:var(--green);transform:translateY(-50%)}
.bar{position:absolute;left:56px;height:5.4px;background:var(--orange);font-size:3.6px;font-weight:600;color:#3a2a00;display:flex;align-items:center;padding-left:6px;white-space:nowrap;transform:translateY(-50%)}
.bar::after{content:"";position:absolute;right:-3.5px;top:-.7px;width:6.6px;height:6.6px;border-radius:50%;background:#fff;border:.6px solid var(--orange)}
/* material cards */
.mat{position:absolute;padding:6px 0 0 22px}
.mat .ico{width:22px;height:19px;background:var(--green);border-radius:2px;margin-bottom:7px}
.mat h4{font-size:6.6px;font-weight:600}
.mat p{font-size:4.3px;color:#444;line-height:1.6}
.mat strong{display:block;font-size:7.4px;font-weight:600;color:var(--green);margin-top:1px}
.numbox{position:absolute;width:21px;height:18px;background:var(--green);color:#fff;font-size:6px;display:flex;align-items:center;justify-content:center}
.impact-text{position:absolute;font-size:4.1px;line-height:1.6;color:#444;width:70px}
</style>
</head>
<body>

<!-- 1. Cover -->
<section class="slide col-a row-1" style="background:#1f3a22">
  <div class="photo" role="img" aria-label="Person in a green shirt holding a recycling box, soft outdoor background" style="inset:0;background:radial-gradient(circle at 50% 70%,#3f6b3d,#14241a 75%)"></div>
  <div class="abs" style="left:35px;top:28px;width:274px;height:137px;background:rgba(58,170,63,.93)"></div>
  <div class="abs" style="left:146px;top:28px;width:52px;height:8px;background:var(--orange)"></div>
  <div class="abs" style="left:0;width:344px;top:62px;text-align:center;font-size:3.6px;font-weight:600;letter-spacing:1.2px;color:var(--orange)">TRELVON VENTURES</div>
  <div class="abs" style="left:0;width:344px;top:79px;text-align:center;font-size:15px;font-weight:600;line-height:1.22;color:#fff">BORACAY RECYCLING<br>PLANT <span style="color:var(--orange)">2026</span></div>
  <div class="abs" style="left:0;width:344px;top:125px;text-align:center;font-size:5px;line-height:1.55;color:#fff"><span style="color:var(--orange)">“</span>Reclaiming Our Islands. Rebuilding Our<br>Economy<span style="color:var(--orange)">”</span></div>
</section>

<!-- 2. Investor Hook -->
<section class="slide col-b row-1">
  <div class="brand"><i></i>TRELVON VENTURES</div>
  <div class="tag"></div>
  <div class="abs title" style="left:0;width:344px;top:14px;text-align:center"><em>The</em> Investor Hook</div>
  <div class="rule" style="left:164px;top:31px"></div>
  <div class="abs" style="left:0;width:344px;top:40px;text-align:center;font-size:6.6px;font-weight:600;color:var(--green-dark)">The Philippines Has 7,700+ Islands But Who Controls Their Infrastructure?</div>
  <div class="btn" style="left:38px;top:52px;width:54px;height:18px;font-size:4px;justify-content:flex-start;padding-left:4px;line-height:1.2">Boracay alone<br>produces: &nbsp;→</div>
  <div class="abs small" style="left:102px;top:55px;color:#333"><b>36,500</b> tons of plastic<br>waste annually.</div>
  <div class="abs" style="left:160px;top:54px;width:.5px;height:14px;background:#ccc"></div>
  <div class="abs small" style="left:181px;top:55px;color:#333"><b>100 tons</b><br>per day.</div>
  <div class="abs" style="left:225px;top:54px;width:.5px;height:14px;background:#ccc"></div>
  <div class="abs small" style="left:234px;top:54px;color:#333">Only <b>40–50%</b> effectively<br>collected</div>
  <div class="photo" role="img" aria-label="Faded photo of hands holding a small plant and pen over documents" style="left:0;top:81px;width:344px;height:112px;background:linear-gradient(180deg,#e8ece8,#f3f3f1)"></div>
  <div class="btn" style="left:135px;top:81px;width:72px;height:18px;font-size:6px">Now Imagine...</div>
  <div class="check-row" style="left:43px;top:113px"><span class="tick"></span><span>A fully Filipino-controlled recycling infrastructure</span></div>
  <div class="check-row" style="left:43px;top:132px"><span class="tick"></span><span>Profits staying inside the islands</span></div>
  <div class="check-row" style="left:43px;top:151px;width:110px"><span class="tick"></span><span>Circular economy built by island-minded investors</span></div>
  <div class="check-row" style="left:183px;top:114px"><span class="tick"></span><span>5 Major Tourist Islands</span></div>
  <div class="check-row" style="left:183px;top:133px"><span class="tick"></span><span>$75–85M investment per island</span></div>
  <div class="check-row" style="left:183px;top:152px;width:128px"><span class="tick"></span><span>$75M+ projected annual profits from 5 islands (TV + operations combined)</span></div>
  <div class="pageno">2<i></i></div>
</section>

<!-- 3. Island Opportunity -->
<section class="slide col-a row-2">
  <div class="brand"><i></i>TRELVON VENTURES</div>
  <div class="abs title" style="left:13px;top:31px"><em>The Island</em><br>Opportunity</div>
  <div class="rule" style="left:14px;top:67px"></div>
  <div class="abs" style="left:15px;top:73px;width:23px;height:19px;background:var(--green);border-radius:2px"></div>
  <div class="abs" style="left:18px;top:98px;font-size:7px;font-weight:600;line-height:1.2;color:var(--green-dark)">Top 5 Tourist<br>Islands Targeted:</div>
  <ol class="abs" style="left:26px;top:117px;font-size:4.2px;font-weight:600;line-height:1.85;color:#333">
    <li>Boracay</li><li>Palawan</li><li>Siquijor</li><li>Bohol</li><li>Siargao</li>
  </ol>
  <div class="abs" style="left:123px;top:38px;width:.6px;height:30px;background:#ddd"></div>
  <div class="abs small" style="left:133px;top:43px;width:170px;color:#333">These islands host millions of tourists annually — yet rely heavily on imported bottled water, construction materials, and foreign-controlled supply chains. We reverse that.</div>
  <div class="photo" role="img" aria-label="Plastic water bottle product shot" style="left:309px;top:5px;width:26px;height:59px;border-radius:8px 8px 4px 4px;background:linear-gradient(90deg,#dfe3e6,#f7f8f9,#d4d9dc)"></div>
  <div class="photo" role="img" aria-label="Volunteers in green shirts collecting litter in an autumn park" style="left:123px;top:70px;width:221px;height:123px;background:linear-gradient(180deg,#7d7a4e 0%,#8c8a63 35%,#e9efe6 38%,#eef2ed 100%)"></div>
  <div class="btn" style="left:123px;top:102px;width:34px;height:18px;font-size:6.5px;border-radius:0 0 6px 0">We</div>
  <div class="abs" style="left:140px;top:136px;width:200px;display:flex;justify-content:space-between;font-size:4.1px;font-weight:600;text-align:center;color:#333;line-height:1.6">
    <div style="width:30px"><div style="width:8px;height:6px;margin:0 auto 3px;border:.8px solid var(--blue)"></div>Collect<br>locally</div>
    <div style="width:30px"><div style="width:8px;height:6px;margin:0 auto 3px;border:.8px dashed var(--blue)"></div>Distribute<br>locally</div>
    <div style="width:30px"><div style="width:7px;height:7px;margin:0 auto 2px;border:.8px solid var(--blue);border-radius:50%"></div>Process<br>locally</div>
    <div style="width:30px"><div style="width:8px;height:6px;margin:0 auto 3px;border-radius:3px;background:var(--blue)"></div>Keep profits<br>local</div>
    <div style="width:36px"><div style="width:7px;height:7px;margin:0 auto 2px;border:1.4px dotted var(--blue);border-radius:50%"></div>Manufacture<br>locally</div>
  </div>
  <div class="pageno">3<i></i></div>
</section>

<!-- 4. Why This Wins -->
<section class="slide col-b row-2">
  <div class="brand"><i></i>TRELVON VENTURES</div>
  <div class="abs title" style="left:13px;top:24px"><em>Why</em> This Wins</div>
  <div class="rule" style="left:15px;top:41px"></div>
  <div class="abs" style="left:17px;top:47px;font-size:7px;font-weight:600;color:var(--green-dark)">Boracay Water Bottle Economics</div>
  <ol class="abs" style="left:25px;top:63px;font-size:4.1px;font-weight:600;line-height:1.87;color:#222">
    <li>Tourists = 2,200,000 /Year</li>
    <li>People =6,043 /day</li>
    <li>1,500 plastic water bottles consumed daily</li>
    <li>Recycling plant produces:1,500 rebottled</li>
    <li>1,500 reserve bottles= 3,000 /day</li>
    <li>21,000 bottles per week@ 100 pesos per bottle</li>
    <li>= 2,100,000 pesos /week</li>
    <li>= $35,901.77 USD /week</li>
    <li>= $2,074,892.04 USD /year</li>
  </ol>
  <div class="abs" style="left:142px;top:32px;width:202px;height:117px;background:var(--panel)"></div>
  <div class="photo" role="img" aria-label="Large clear plastic water bottle with a small label" style="left:150px;top:31px;width:52px;height:130px;border-radius:16px 16px 10px 10px;background:linear-gradient(90deg,#d6dadd,#f8f9fa 45%,#cfd4d8)"></div>
  <div class="abs" style="left:215px;top:64px;font-size:7.4px;font-weight:600;line-height:1.75;color:var(--green)">Multiply by 5 islands =<br>$10,374,460.20 USD<br>annually (water only)</div>
  <div class="btn" style="left:213px;top:106px;width:98px;height:18px;font-size:6.4px">And that’s only plastics.</div>
  <div class="pageno">4<i></i></div>
</section>

<!-- 5. Budget -->
<section class="slide col-a row-3">
  <div class="brand"><i></i>TRELVON VENTURES</div>
  <div class="abs title" style="left:13px;top:24px"><em>Budget</em> Expenditure</div>
  <div class="rule" style="left:15px;top:41px"></div>
  <div class="abs" style="left:15px;top:46px;width:295px;height:122px;background:var(--panel)"></div>
  <div class="bar-label" style="top:58px">$40M+</div><div class="bar" style="top:58px;width:247px">SPR BORACAY – BUY LANDSITE</div>
  <div class="bar-label" style="top:68.3px">$15M</div><div class="bar" style="top:68.3px;width:225px">CONSTRUCTION OF RECYCLING PLANT</div>
  <div class="bar-label" style="top:78.6px">$10M</div><div class="bar" style="top:78.6px;width:203px">EARTHMOVING / EXCAVATIONS</div>
  <div class="bar-label" style="top:88.9px">$10M</div><div class="bar" style="top:88.9px;width:203px">RECYCLING EQUIPMENT•</div>
  <div class="bar-label" style="top:99.2px">$5M</div><div class="bar" style="top:99.2px;width:139px">RESERVE PETTY CASH</div>
  <div class="bar-label" style="top:109.5px">$5M</div><div class="bar" style="top:109.5px;width:139px">TV FILM &amp; PRODUCTIONS</div>
  <div class="bar-label" style="top:119.8px">$1M</div><div class="bar" style="top:119.8px;width:98px">UTILITIES (Power/Water/Etc)</div>
  <div class="bar-label" style="top:130.1px">$1M</div><div class="bar" style="top:130.1px;width:98px">SHIPPING COSTS</div>
  <div class="bar-label" style="top:140.4px">$500K</div><div class="bar" style="top:140.4px;width:66px">EMPLOYMENT TEAMs</div>
  <div class="bar-label" style="top:150.7px">$380K</div><div class="bar" style="top:150.7px;width:52px">TRANSPORTATION</div>
  <div class="bar-label" style="top:161px">$250K</div><div class="bar" style="top:161px;width:36px;font-size:2.8px">APPOINTED TEAM</div>
  <div class="btn" style="left:240px;top:143px;width:71px;height:28px;border-radius:4px;flex-direction:column;line-height:1.15">
    <span style="font-size:3.6px;font-weight:500">TOTAL EXPENDITURE:</span>
    <span style="font-size:10px">$88.13M</span>
  </div>
  <div class="pageno">5<i></i></div>
</section>

<!-- 6. Recycling Plant Focus -->
<section class="slide col-b row-3">
  <div class="brand"><i></i>TRELVON VENTURES</div>
  <div class="tag"></div>
  <div class="abs title" style="left:13px;top:24px"><em>Recycling</em> Plant<br>Focus</div>
  <div class="rule" style="left:15px;top:57px"></div>
  <div class="abs" style="left:20px;top:126px;display:flex;align-items:center;gap:4px;font-size:8px;font-weight:600;line-height:1.15;color:var(--green)">
    <span style="width:12px;height:12px;border-radius:50%;background:var(--orange)"></span>TRELVON<br>VENTURES
  </div>
  <div class="abs" style="left:124px;top:26px;width:214px;height:147px;background:#1b1b1b;border-radius:6px 6px 0 0"></div>
  <div class="abs" style="left:118px;top:172px;width:230px;height:4px;background:linear-gradient(#cfcfcf,#8a8a8a);border-radius:0 0 4px 4px"></div>
  <div class="abs" style="left:133px;top:36px;width:197px;height:128px;background:#fff"></div>
  <div class="abs" style="left:133px;top:41px;width:197px;text-align:center;font-size:7px;font-weight:600;letter-spacing:.3px;color:#555">PRODUCTION TURNOVER:</div>
  <svg class="abs" style="left:133px;top:36px" width="197" height="128" viewBox="0 0 197 128">
    <g stroke="#e6e6e6" stroke-width=".6"><line x1="66" y1="20" x2="66" y2="113"/><line x1="130" y1="20" x2="130" y2="113"/><line x1="6" y1="113" x2="191" y2="113"/></g>
    <rect x="28" y="26" width="12" height="87" fill="#f9ae3b"/>
    <rect x="92" y="60" width="12" height="53" fill="#f9ae3b"/>
    <rect x="156" y="99" width="12" height="14" fill="#f9ae3b"/>
    <g fill="#3aaa3f"><circle cx="34" cy="26" r="9"/><circle cx="98" cy="60" r="9"/><circle cx="162" cy="99" r="9"/></g>
    <g fill="#fff" font-family="Poppins,sans-serif" font-size="6" font-weight="600" text-anchor="middle"><text x="34" y="28">60%</text><text x="98" y="62">35%</text><text x="162" y="101">5%</text></g>
    <g fill="#333" font-family="Poppins,sans-serif" font-size="4.2" font-weight="600" letter-spacing=".4" text-anchor="middle"><text x="34" y="120">PLASTICS</text><text x="98" y="120">GLASS</text><text x="162" y="120">PAPER / CARDBOARD</text></g>
  </svg>
  <div class="pageno">6<i></i></div>
</section>

<!-- 7. Profit by Material -->
<section class="slide col-a row-4">
  <div class="brand"><i></i>TRELVON VENTURES</div>
  <div class="tag"></div>
  <div class="abs title" style="left:0;width:344px;top:29px;text-align:center"><em>Profit Breakdown</em> By Material</div>
  <div class="rule" style="left:164px;top:47px"></div>
  <div class="photo" role="img" aria-label="Faded photo of volunteers collecting plastic waste" style="left:0;top:56px;width:115px;height:94px;background:linear-gradient(135deg,#e3ede0,#f1f5ef)"></div>
  <div class="photo" role="img" aria-label="Faded photo of volunteers sorting glass waste" style="left:115px;top:67px;width:114px;height:95px;background:linear-gradient(135deg,#e6ebe3,#f3f5f1)"></div>
  <div class="photo" role="img" aria-label="Faded photo of volunteers collecting cardboard and paper" style="left:229px;top:81px;width:115px;height:94px;background:linear-gradient(135deg,#e3ede0,#f2f5f0)"></div>
  <div class="mat" style="left:0;top:63px"><div class="ico"></div><h4>Plastics (60%)</h4><p>Approximate yearly profits:</p><strong>$10M+ per year</strong></div>
  <div class="mat" style="left:103px;top:74px"><div class="ico"></div><h4>Glass (35%)</h4><p style="font-size:3.8px;line-height:1.7">Recycled into:<br>Bricks / Pavers / Building Products</p><p>Approximate yearly profits:</p><strong>$5–10M per year</strong></div>
  <div class="mat" style="left:216px;top:88px"><div class="ico"></div><h4>Paper / Cardboard (5%)</h4><p style="font-size:3.8px;line-height:1.7">Schools / NGOs (Tax Exempt)<br>Office Supplies (15% chargeable)</p><p>Approximate yearly profits:</p><strong>$1–3M per year</strong></div>
  <div class="pageno">7<i></i></div>
</section>

<!-- 8. ROI & Exit -->
<section class="slide col-b row-4">
  <div class="brand"><i></i>TRELVON VENTURES</div>
  <div class="tag"></div>
  <div class="photo" role="img" aria-label="Very faint photo of recycling boxes and bottles" style="left:234px;top:0;width:110px;height:193px;background:linear-gradient(180deg,#f3f4f1,#faf8f0)"></div>
  <div class="abs title" style="left:13px;top:24px"><em>ROI &amp;</em> Exit Strategy</div>
  <div class="rule" style="left:15px;top:43px"></div>
  <div class="abs" style="left:15px;top:46px;font-size:7px;font-weight:600;color:var(--green-dark)">Expected ROI Timeline</div>
  <div class="abs small" style="left:15px;top:57px;width:175px;color:#333">Return on Investment expected to be achieved by year 5–7 &amp; even more achievable in less time via private investing influenced by market &amp; operational efficiency.</div>
  <svg class="abs" style="left:0;top:95px" width="200" height="80" viewBox="0 0 200 80">
    <line x1="37" y1="25" x2="155" y2="25" stroke="#f9ae3b" stroke-width=".6" stroke-dasharray="2 1.5"/>
    <g fill="#f9ae3b"><circle cx="37" cy="25" r="3.4"/><circle cx="97" cy="25" r="3.4"/><circle cx="155" cy="25" r="3.4"/></g>
    <g fill="none" stroke="#fff" stroke-width=".7"><path d="M35.6 25l1 1 2-2"/><path d="M95.6 25l1 1 2-2"/><path d="M153.6 25l1 1 2-2"/></g>
  </svg>
  <div class="abs" style="left:22px;top:100px;width:30px;text-align:center;font-size:6px;font-weight:500;line-height:1;color:var(--green)">8–10<br><span style="font-size:4px">months</span></div>
  <div class="abs" style="left:82px;top:99px;width:30px;text-align:center;font-size:6px;font-weight:500;line-height:1.2;color:var(--green)">3<br>year</div>
  <div class="abs" style="left:140px;top:99px;width:30px;text-align:center;font-size:6px;font-weight:500;line-height:1.2;color:var(--green)">6<br>year</div>
  <div class="abs" style="left:20px;top:140px;width:37px;text-align:center;font-size:5.2px;font-weight:500;line-height:1.3">Revenue Generation Begins</div>
  <div class="abs" style="left:80px;top:129px;width:27px;height:34px;background:#fff;box-shadow:0 1px 3px rgba(0,0,0,.12);text-align:center;font-size:2.8px;font-weight:600;line-height:1.2">
    <svg width="20" height="20" viewBox="0 0 20 20" style="display:block;margin:2px auto 1px"><circle cx="10" cy="10" r="8" fill="none" stroke="#e5e5e5" stroke-width="1.6"/><path d="M10 2a8 8 0 0 1 7.6 5.5" fill="none" stroke="#3aaa3f" stroke-width="1.6"/><text x="10" y="11" font-family="Poppins,sans-serif" font-size="3" text-anchor="middle" fill="#333">20–25%</text></svg>Profit Margin<br>Growth</div>
  <div class="abs" style="left:138px;top:129px;width:27px;height:34px;background:#fff;box-shadow:0 1px 3px rgba(0,0,0,.12);text-align:center;font-size:2.8px;font-weight:600;line-height:1.2">
    <svg width="20" height="20" viewBox="0 0 20 20" style="display:block;margin:2px auto 1px"><circle cx="10" cy="10" r="8" fill="none" stroke="#e5e5e5" stroke-width="1.6"/><path d="M10 2a8 8 0 1 1-6 13.3" fill="none" stroke="#3aaa3f" stroke-width="1.6"/><text x="10" y="11" font-family="Poppins,sans-serif" font-size="3" text-anchor="middle" fill="#333">40–50%</text></svg>Profit Margin<br>Growth</div>
  <div class="abs" style="left:78px;top:164px;width:31px;text-align:center;font-size:5.4px;font-weight:600">20–25%</div>
  <div class="abs" style="left:136px;top:164px;width:31px;text-align:center;font-size:5.4px;font-weight:600">40–50%</div>
  <div class="abs" style="left:214px;top:97px;width:130px;height:53px;background:var(--green);border-radius:7px 0 0 7px;color:#fff;padding:7px 0 0 15px">
    <div style="font-size:7px;font-weight:600;margin-bottom:2px">Exit Strategies</div>
    <ol style="font-size:4.3px;line-height:1.7;padding-left:6px"><li>Sales to Waste Management firms</li><li>Acquisition by sustainability investors</li></ol>
  </div>
  <div class="abs" style="left:340px;top:150px;width:4px;height:43px;background:var(--orange)"></div>
  <div class="pageno" style="right:16px">8<i></i></div>
</section>

<!-- 9. Impact -->
<section class="slide col-a row-5">
  <div class="brand"><i></i>TRELVON VENTURES</div>
  <div class="tag"></div>
  <div class="abs title" style="left:0;width:344px;top:22px;text-align:center"><em>Environmental &amp;</em> National Impact</div>
  <div class="rule" style="left:164px;top:39px"></div>
  <svg class="abs" style="left:0;top:0" width="344" height="193" viewBox="0 0 344 193">
    <g fill="none" stroke="#555" stroke-width=".5">
      <path d="M131 73l8 -6h-4"/><path d="M131 73l-5-5h-6"/>
      <path d="M141 110h-20"/>
      <path d="M135 147l-9 8h-6"/>
      <path d="M210 73l9-6h6"/>
      <path d="M201 110h20"/>
      <path d="M207 147l9 8h6"/>
    </g>
    <g fill="#555"><circle cx="120" cy="68" r="1"/><circle cx="121" cy="110" r="1"/><circle cx="120" cy="155" r="1"/><circle cx="225" cy="67" r="1"/><circle cx="221" cy="110" r="1"/><circle cx="222" cy="155" r="1"/></g>
    <g fill="none" stroke-width="3">
      <path d="M140 86a36 36 0 0 1 29-12" stroke="#f9ae3b"/>
      <path d="M174 74a36 36 0 0 1 29 16" stroke="#e5262b"/>
      <path d="M206 95a36 36 0 0 1 -3 30" stroke="#2a9fe0"/>
      <path d="M200 130a36 36 0 0 1 -27 16" stroke="#f9ae3b"/>
      <path d="M167 146a36 36 0 0 1 -28 -16" stroke="#e5262b"/>
      <path d="M136 124a36 36 0 0 1 0 -30" stroke="#2a9fe0"/>
    </g>
    <circle cx="171" cy="110" r="27" fill="#fff" stroke="#ececec" stroke-width=".6"/>
  </svg>
  <div class="abs" style="left:144px;top:105px;width:54px;text-align:center;font-size:5px;font-weight:600;line-height:1.15;color:var(--green)">TRELVON<br>VENTURES</div>
  <div class="numbox" style="left:96px;top:53px">01</div>
  <div class="numbox" style="left:96px;top:94px">02</div>
  <div class="numbox" style="left:96px;top:135px">03</div>
  <div class="numbox" style="left:227px;top:53px">03</div>
  <div class="numbox" style="left:227px;top:94px">04</div>
  <div class="numbox" style="left:227px;top:135px">05</div>
  <div class="impact-text" style="left:46px;top:76px;text-align:right">Diverts millions of kilograms of plastic annually</div>
  <div class="impact-text" style="left:46px;top:116px;text-align:right">Reduces marine<br>pollution</div>
  <div class="impact-text" style="left:46px;top:157px;text-align:right">Strengthens LGU<br>compliance</div>
  <div class="impact-text" style="left:227px;top:76px">Creates 20+ direct jobs per island</div>
  <div class="impact-text" style="left:227px;top:115px">Empowers informal recycling sector</div>
  <div class="impact-text" style="left:227px;top:156px">Supports Circular<br>Economy model</div>
  <div class="pageno">9<i></i></div>
</section>

<!-- 10. Final Message -->
<section class="slide col-b row-5">
  <div class="abs" style="left:120px;top:165px;width:224px;height:28px;background:var(--green)"></div>
  <div class="abs" style="left:300px;top:62px;width:44px;height:131px;background:var(--green)"></div>
  <div class="photo" role="img" aria-label="Dark-toned photo of hands holding a small plant and a pen over paperwork" style="left:0;top:0;width:300px;height:165px;background:linear-gradient(135deg,#3a3d3a,#232523)"></div>
  <div class="tag"></div>
  <div class="abs" style="left:21px;top:55px;width:128px;text-align:center;font-size:6px;font-weight:600;letter-spacing:2px;color:var(--orange)">TRELVON VENTURES</div>
  <div class="abs" style="left:24px;top:66px;font-size:34px;font-weight:700;line-height:1;color:var(--orange)">“</div>
  <div class="abs" style="left:54px;top:81px;font-size:13.4px;font-weight:600;color:#fff">Final Message to Investors</div>
  <div class="abs" style="left:54px;top:104px;font-size:6.6px;line-height:1.9;color:var(--orange)">An Investment of a Lifetime Opportunity<br>for Global Expansion.</div>
</section>

</body>
</html>
```